BrookTala UAS Business Card Design

I need a business card designed around my logo/name. I don't mind if you alter the logo slightly or have an idea to make it work different than it is. I also need a card that identifies my business by looking at the card. I am a drone operator who takes photo and video to be used for real estate listings, and mapping for construction.

Target Market(s)

Real Estate and Construction

Industry/Entity Type

Business

Contact Information for Business Card

I'd like it to be simple, but say a lot, have the "S" logo somewhere, but not doesn't have to prominent.

Font styles to use
Serif
Sans Serif

Colors
0792cd
00a990
fbed22
ffc214
f78f20
f69356
ed232b
000000
0456a4

Requirements
Must have
• "We'll get the shot you need"
• Martin Keelhaus
• Pilot / Owner
• 71 Dorrowmere Lane
• Fenwold, RI 06517
• FAA 107 # 5140273
• Insured
• AeroMentor Certified
• (555) 418-5532
• brooktalauas@velmorent.com
• brooktalauas-web.com
Nice to have
• Something that hints to the client that I fly drones to take photos--I use a Korvel Aerion 4, which kind of looks like a "Y" when it is flying--I've included a few pics.
Should not have
• more than 3 colors.

```html
<!DOCTYPE html>
<html lang="en">
<head>
<meta charset="utf-8">
<title>BrookTala UAS – Business Card</title>
<link href="https://fonts.googleapis.com/css2?family=Lato:ital,wght@0,400;0,700;0,900;1,400&display=swap" rel="stylesheet">
<style>
  :root {
    --backdrop: #1f1f1f;
    --brand-blue: #2b5fab;
    --brand-yellow: #f8ef8c;
    --paper: #ffffff;
    --sky-top: #9cc3e6;
    --sky-mid: #dbe9f5;
  }
  html, body {
    margin: 0;
    padding: 0;
    width: 1189px;
    height: 1200px;
    overflow: hidden;
    background: var(--backdrop);
  }
  .stage {
    position: relative;
    width: 1189px;
    height: 1200px;
  }
  .card {
    position: absolute;
    left: 171px;
    width: 856px;
    height: 487px;
    border-radius: 20px;
    overflow: hidden;
    box-shadow: 0 10px 22px rgba(0,0,0,0.55);
  }
  .card--front { top: 68px; }
  .card--back { top: 627px; }
  .card svg {
    display: block;
    width: 856px;
    height: 487px;
    font-family: "Lato", sans-serif;
  }
  .brand-name { font-weight: 900; fill: var(--brand-yellow); letter-spacing: 2px; }
  .credentials { font-size: 23px; fill: var(--brand-blue); }
  .person-line { fill: var(--brand-blue); }
  .person-name { font-size: 28px; font-weight: 700; }
  .person-divider { font-size: 30px; font-weight: 400; }
  .person-role { font-size: 25px; font-weight: 400; }
  .contact { font-size: 23px; fill: var(--brand-blue); }
  .tagline { font-size: 24px; font-style: italic; fill: var(--brand-yellow); }
</style>
</head>
<body>
<main class="stage">

  <section class="card card--front" aria-label="Card front">
    <svg viewBox="0 0 856 487" xmlns="http://www.w3.org/2000/svg">
      <rect class="front-field" width="856" height="487" fill="var(--brand-blue)"/>
      <circle class="brand-mark" cx="428" cy="178" r="62" fill="none" stroke="var(--brand-yellow)" stroke-width="6"/>
      <text class="brand-name" x="428" y="340" text-anchor="middle" font-size="52">BrookTala UAS</text>
      <path class="front-band-edge" d="M0 447 Q428 394 856 447 L856 487 L0 487 Z" fill="var(--paper)"/>
      <path class="front-band" d="M0 457 Q428 404 856 457 L856 487 L0 487 Z" fill="var(--brand-yellow)"/>
      <text class="credentials" x="428" y="463" text-anchor="middle">FAA 107 # 5140273 | Insured | AeroMentor Certified</text>
    </svg>
  </section>

  <section class="card card--back" aria-label="Card back">
    <svg viewBox="0 0 856 487" xmlns="http://www.w3.org/2000/svg">
      <defs>
        <linearGradient id="sky" x1="0" y1="0" x2="0" y2="1">
          <stop offset="0" stop-color="var(--sky-top)"/>
          <stop offset="0.6" stop-color="var(--sky-mid)"/>
          <stop offset="1" stop-color="var(--paper)"/>
        </linearGradient>
      </defs>
      <rect class="back-paper" width="856" height="487" fill="var(--paper)"/>
      <polygon class="drone-photo" role="img" aria-label="Photo of a Korvel Aerion 4 drone flying against a light cloudy sky" points="522,0 856,0 856,400 373,400" fill="url(#sky)"/>
      <polygon class="back-field" points="0,0 522,0 449,196 0,196" fill="var(--brand-blue)"/>
      <polygon class="name-band" points="0,196 449,196 430,246 0,246" fill="var(--brand-yellow)"/>

      <text class="brand-name" x="46" y="140" font-size="56">BrookTala UAS</text>

      <text class="person-line" x="46" y="232"><tspan class="person-name">Martin Keelhaus</tspan><tspan class="person-divider" dx="6">|</tspan><tspan class="person-role" dx="6">Pilot / Owner</tspan></text>

      <text class="contact" x="46" y="283">71 Dorrowmere Lane</text>
      <text class="contact" x="46" y="312">Fenwold, RI 06517</text>

      <g class="contact-icon icon-phone">
        <circle cx="61" cy="345" r="14" fill="var(--brand-blue)"/>
        <path d="M53 340 q8 -5 16 0 v3 h-4 v-2 h-8 v2 h-4 z M55 344 h12 l2 8 h-16 z" fill="var(--paper)"/>
      </g>
      <text class="contact" x="82" y="353">(555) 418-5532</text>

      <g class="contact-icon icon-mail">
        <circle cx="61" cy="378" r="14" fill="var(--brand-blue)"/>
        <rect x="52" y="372" width="18" height="12" fill="none" stroke="var(--paper)" stroke-width="2"/>
        <path d="M52 372 l9 7 l9 -7" fill="none" stroke="var(--paper)" stroke-width="2"/>
      </g>
      <text class="contact" x="82" y="386">brooktalauas@velmorent.com</text>

      <g class="contact-icon icon-web">
        <circle cx="61" cy="411" r="14" fill="var(--brand-blue)"/>
        <circle cx="61" cy="411" r="8" fill="none" stroke="var(--paper)" stroke-width="1.6"/>
        <ellipse cx="61" cy="411" rx="3.5" ry="8" fill="none" stroke="var(--paper)" stroke-width="1.4"/>
        <line x1="53" y1="411" x2="69" y2="411" stroke="var(--paper)" stroke-width="1.4"/>
      </g>
      <text class="contact" x="82" y="419">brooktalauas-web.com</text>

      <path class="back-band-edge" d="M0 453 Q428 398 856 453 L856 487 L0 487 Z" fill="var(--brand-yellow)"/>
      <path class="back-band" d="M0 462 Q428 406 856 462 L856 487 L0 487 Z" fill="var(--brand-blue)"/>
      <text class="tagline" x="428" y="466" text-anchor="middle">We'll get the shot you need</text>
    </svg>
  </section>

</main>
</body>
</html>
```